Solar Power Promotion September 15

Meadowlark Energies - A provider of renewable energy solutions. I need a flyer that will be mailed and emailed out to businesses to educate them about the Solar Power Business opportunities which are out there but which the government will soon be removing. Key details are as follows:
Solar Panel Flyer
The Governments Policy on Renewable Energy is changing.
In recent years they have heavily subsidized the industry to encourage investment. Now larger installations, for example Solar Farms, are no longer encouraged. For smaller installations of 10 kilowatts to 250 kilowatts, most suitable for SMEs, these subsidies will be dropping soon so we would encourage you to call us on 0161 492 8306 with a view to arranging an appointment with one of our specialist advisers. They will discuss your requirements and guide you in understanding how renewable energy solutions can help your business reduce its energy costs.

Why Renewable Energy Solutions?- The sun for example emits thousands of times more energy than humans actually need- Renewable Energy resources are potentially limitless, in stark contrast to standard energy sources which are rapidly depleting- Solar power stations and other forms of renewable energy are secure dividends, not only for the environment but because of state subsidy programmes for you- You use less power from your expensive energy provider- You protect yourself against future price rises- Demonstrate your companies environmental credentials to customers and stakeholdersWhy Meadowlark Energies?- Nationwide reputation for excellence with offices in Wigan, Bury, Edinburgh, Glasgow and Cornwall.- To date we have installed over 4 megawatts (MW) of Solar Photovolatics (PV). This is equivalent to 1300 installations of 30 kilowatts (KW)- Our quality is second to none, we have been awarded the Crest Honour award from the Allied Assurance Guild, with a 99% customer approval rating for the last 2 years.- We offer a variety of flexible solutions which will enable every business unlock the potential of renewable energy solutions. This includes, free to fit solar on generous power purchase agreements, outright purchase and financed options on competitive rates which enable swift capital repayment on your investment.Your Benefits- Reduced electricity bills- Clean solar energy, with options for zero upfront investment- Lower operational costs- Consuming solar power on site- Protection against increasing energy costsEvery business is different so we would encourage you to call us today to arrange a free, no obligation survey so that you can take advantage of the governments generous renewable energy subsidies before the next reduction.

The best designs will incorporate a strong call to action email - info@meadowlarkenergies.example and telephone - 0161 763 4157The target customers are people who own their buildingEnquiries should quote "September15" as a reference Added Thursday, August 27, 2015

Target Market(s)

Building Owners who own their own building

Industry/Entity Type

Construction

Font styles to use
Sans Serif

Requirements
Must have
• Strong Call to action. Pictures of renewable energy solutions, copy of our logo
Nice to have
• Something similar in style to the website but including the information from the product brief.
• The text from the above description after the phrase "Key details are as follows:
• Solar Panel Flyer"
Should not have
• Any of the text in the above project description including and before the phrase "Key details are as follows:
• Solar Panel Flyer"

```html
<!DOCTYPE html>
<html lang="en">
<head>
<meta charset="utf-8">
<title>Meadowlark Energies – Solar Power Flyer</title>
<link rel="stylesheet" href="https://fonts.googleapis.com/css2?family=Open+Sans:wght@400;600;700;800&display=swap">
<style>
  :root {
    --green: #5aa62e;
    --ink: #2d2d2d;
    --muted: #555b60;
    --white: #ffffff;
    --sky-top: #6f9fc9;
    --sky-low: #c9d8e3;
    --panel: #2c3c55;
  }
  * { box-sizing: border-box; margin: 0; padding: 0; }
  html, body { width: 843px; height: 1200px; overflow: hidden; background: var(--white); }
  body { font-family: "Open Sans", Arial, sans-serif; color: var(--ink); }
  .flyer { position: relative; width: 843px; height: 1200px; overflow: hidden; background: var(--white); }

  .masthead { position: absolute; top: 0; left: 0; width: 843px; height: 150px; }
  .brand { position: absolute; left: 40px; top: 34px; }
  .brand-row { display: flex; align-items: center; gap: 12px; }
  .brand-mark { width: 40px; height: 40px; border-radius: 50%; background: var(--green); }
  .brand-name { font-size: 32px; font-weight: 700; color: var(--ink); line-height: 1; letter-spacing: -0.5px; }
  .brand-tagline { margin-top: 10px; font-size: 10px; font-weight: 700; color: var(--green); letter-spacing: 1.1px; text-transform: uppercase; }

  .call-block { position: absolute; right: 40px; top: 18px; }
  .call-title { font-size: 28px; font-weight: 800; color: var(--green); line-height: 1.15; }
  .call-title em { font-style: normal; color: var(--ink); }
  .call-phone { display: flex; align-items: center; gap: 8px; margin-top: 6px; font-size: 22px; font-weight: 700; color: var(--green); line-height: 1.2; }
  .call-phone svg { width: 22px; height: 22px; }
  .call-quote { font-size: 17px; font-weight: 600; color: var(--ink); margin-top: 6px; line-height: 1.2; }

  .hero { position: absolute; top: 150px; left: 0; width: 843px; height: 440px;
    background: linear-gradient(180deg, var(--sky-top) 0%, var(--sky-low) 18%, #8aa0b6 32%, var(--panel) 55%, #3c4d63 80%, #4f6a4a 100%); }
  .hero-banner { position: absolute; top: 180px; left: 40px; width: 763px; padding: 16px 30px;
    background: rgba(30, 36, 42, 0.62); color: var(--white); text-align: center;
    font-size: 27px; font-weight: 600; line-height: 1.35; }

  .intro { position: absolute; top: 590px; left: 0; width: 843px; height: 155px; background: var(--green);
    color: var(--white); padding: 18px 40px; font-size: 13.5px; line-height: 1.45; }
  .intro strong { font-weight: 700; }

  .rooftop { position: absolute; left: 545px; top: 765px; width: 298px; height: 435px;
    background: linear-gradient(180deg, #9fc2df 0%, #d4e2ea 25%, #4a5568 50%, #6d5a4a 72%, #5c8a3e 100%);
    -webkit-mask-image: linear-gradient(90deg, transparent 0%, #000 30%);
    mask-image: linear-gradient(90deg, transparent 0%, #000 30%); }

  .reasons { position: absolute; top: 780px; left: 40px; width: 500px; }
  .reasons-title { font-size: 26px; font-weight: 600; color: var(--ink); margin-bottom: 16px; white-space: nowrap; }
  .reasons-title span { color: var(--green); font-weight: 800; }
  .reasons-list { list-style: none; }
  .reasons-list li { display: flex; gap: 10px; font-size: 14px; line-height: 1.4; color: var(--muted); margin-bottom: 9px; }
  .reasons-list svg { flex: 0 0 18px; width: 18px; height: 18px; margin-top: 1px; }
</style>
</head>
<body>
<div class="flyer">
  <header class="masthead">
    <div class="brand">
      <div class="brand-row">
        <div class="brand-mark"></div>
        <div class="brand-name">Meadowlark Energies</div>
      </div>
      <div class="brand-tagline">Renewable energy solutions for the future</div>
    </div>
    <div class="call-block">
      <div class="call-title">CALL US <em>NOW!</em></div>
      <div class="call-phone">
        <svg viewBox="0 0 24 24" aria-hidden="true"><path fill="#5aa62e" d="M6.6 10.8a15.1 15.1 0 0 0 6.6 6.6l2.2-2.2c.3-.3.7-.4 1-.2 1.1.4 2.3.6 3.6.6.6 0 1 .4 1 1V20c0 .6-.4 1-1 1A17 17 0 0 1 3 4c0-.6.4-1 1-1h3.5c.6 0 1 .4 1 1 0 1.2.2 2.4.6 3.6.1.3 0 .7-.2 1z"/></svg>
        0161 492 8306
      </div>
      <div class="call-quote">Quote: September 15</div>
    </div>
  </header>

  <section class="hero" role="img" aria-label="Photograph of rows of solar panels on a commercial building roof under a blue sky">
    <h1 class="hero-banner">Solar Panel energy solutions can help your business reduce it’s energy costs</h1>
  </section>

  <section class="intro">
    <p>The Governments Policy on Renewable Energy is changing. In recent years they have heavily subsidised the industry to encourage investment. Now larger installations, for example Solar Farms, are no longer encouraged. For smaller installations of 10 kilowatts to 250 kilowatts, most suitable for SME’s, these subsidies will be dropping soon so we would encourage you to call us on <strong>0161 492 8306</strong> with a view to arranging an appointment with one of our specialist advisers. They will discuss your requirements and guide you in understanding how renewable.</p>
  </section>

  <div class="rooftop" role="img" aria-label="Photograph of a house roof fitted with solar panels and a green lawn"></div>

  <section class="reasons">
    <h2 class="reasons-title">Why <span>RENEWABLE ENERGY</span> Solutions?</h2>
    <ul class="reasons-list">
      <li><svg viewBox="0 0 18 18" aria-hidden="true"><rect x="1" y="1" width="16" height="16" rx="2" fill="none" stroke="#5aa62e" stroke-width="1.6"/><path d="M4.5 9.2l3 3 6-6.5" fill="none" stroke="#5aa62e" stroke-width="2.2" stroke-linecap="round"/></svg>The sun for example emits thousands of times more energy than humans actually need.</li>
      <li><svg viewBox="0 0 18 18" aria-hidden="true"><rect x="1" y="1" width="16" height="16" rx="2" fill="none" stroke="#5aa62e" stroke-width="1.6"/><path d="M4.5 9.2l3 3 6-6.5" fill="none" stroke="#5aa62e" stroke-width="2.2" stroke-linecap="round"/></svg>Renewable Energy resources are potentially limitless, in stark contrast to standard energy sources which are rapidly depleting.</li>
      <li><svg viewBox="0 0 18 18" aria-hidden="true"><rect x="1" y="1" width="16" height="16" rx="2" fill="none" stroke="#5aa62e" stroke-width="1.6"/><path d="M4.5 9.2l3 3 6-6.5" fill="none" stroke="#5aa62e" stroke-width="2.2" stroke-linecap="round"/></svg>Solar power stations and other forms of renewable energy are secure dividends, not only for the environment but because of state subsidy programmes for you.</li>
      <li><svg viewBox="0 0 18 18" aria-hidden="true"><rect x="1" y="1" width="16" height="16" rx="2" fill="none" stroke="#5aa62e" stroke-width="1.6"/><path d="M4.5 9.2l3 3 6-6.5" fill="none" stroke="#5aa62e" stroke-width="2.2" stroke-linecap="round"/></svg>You use less power from your expensive energy provider.</li>
      <li><svg viewBox="0 0 18 18" aria-hidden="true"><rect x="1" y="1" width="16" height="16" rx="2" fill="none" stroke="#5aa62e" stroke-width="1.6"/><path d="M4.5 9.2l3 3 6-6.5" fill="none" stroke="#5aa62e" stroke-width="2.2" stroke-linecap="round"/></svg>You protect yourself against future price rises.</li>
      <li><svg viewBox="0 0 18 18" aria-hidden="true"><rect x="1" y="1" width="16" height="16" rx="2" fill="none" stroke="#5aa62e" stroke-width="1.6"/><path d="M4.5 9.2l3 3 6-6.5" fill="none" stroke="#5aa62e" stroke-width="2.2" stroke-linecap="round"/></svg>Demonstrate your companies environmental credentials to customers and stakeholders.</li>
    </ul>
  </section>
</div>
</body>
</html>
```